Flyer design for VIP membership

We need an A4 flyer design for our automotive workshop explaining and advertising to our customers about our VIP membership.

We are a modern and new workshop in New Zealand. I have attached our business card and another design for you to view. Along with company logo. Our colours are black, white and red.

Design needs to stand out and be easy to read.

Design must include the following wording:
___________________________________________________________________--

BRIGHTLANE TOTAL AUTOMOTIVE
VIP
FLEET VEHICLE SERVICING AND MAINTENANCE
Tradie?
Business owner?
Own 3 or more vehicles?
Become an Brightlane VIP member and receive:
• 10% off Vehicle Servicing and Mechanical Repairs
• 10% off Tyres
• Free basic vehicle exterior wash with every job
• Free puncture repairs
• Vehicle Delivery and Pick up
• Vehicle WOF, Service and Wheel Alignment reminders
• Given quick and first choice on all bookings and appointments
• Organise a tow truck to workshop for local break downs

If you’ve got a fleet of vehicles for your business, Brightlane can make it easy for you to stay on top of your servicing and maintenance schedules. We offer peace of mind motoring that ensures your vehicles are safe and reliable at cost effective prices.
Brightlane is your one stop automotive shop. We aim to make your automotive servicing and repairs as easy and painless as possible. We pride ourselves on excellent customer service and quality workmanship in a professional manner at competitive rates, using the latest technology and equipment.

Our services include:
• Vehicle Servicing
• All Mechanical Repairs
• Brakes, steering and suspension
• Transmission and cooling system servicing
• Warrant of fitness inspections
• Safety checks and pre-purchase inspections
• Tyres and wheel alignments
• Puncture repairs
• Mag wheels
• Vehicle Lowering and lift kits
• Automotive diagnostics
• Trailer repairs, maintenance and parts
• Automotive parts and supplies
• 4WD accessories
• Batteries
• And more
Contact us today to enquire about becoming an Brightlane VIP member.
Phone: 07 842 3917
Email: office@brightlaneautomotive-example.co.nz
Website: www.brightlaneautomotive-example.co.nz

```html
<!DOCTYPE html>
<html lang="en">
<head>
<meta charset="utf-8">
<title>Brightlane VIP Fleet Flyer</title>
<link rel="stylesheet" href="https://fonts.googleapis.com/css2?family=Bebas+Neue&family=Open+Sans:wght@400;600;700&display=swap">
<style>
  :root {
    --red: #d2202f;
    --red-dark: #9e1420;
    --white: #ffffff;
    --ink: #141414;
    --stage: #d9d9d7;
    --muted: #d6d6d6;
    --footer: #0e0e0e;
  }
  * { margin: 0; padding: 0; box-sizing: border-box; }
  html, body { width: 1200px; height: 838px; overflow: hidden; }
  body { background: var(--stage); position: relative; font-family: "Open Sans", Arial, sans-serif; color: var(--white); }

  .flyer {
    position: absolute; top: 55px; width: 515px; height: 731px; overflow: hidden;
    background: radial-gradient(ellipse at 50% 55%, #3a3a3a 0%, #222 55%, var(--ink) 100%);
    box-shadow: 0 6px 18px rgba(0,0,0,.35);
  }
  .flyer--front { left: 55px; }
  .flyer--back { left: 634px; }

  .art { position: absolute; left: 0; top: 0; width: 515px; height: 731px; }

  .brand {
    position: absolute; top: 12px; left: 0; width: 100%; text-align: center;
    font-family: "Bebas Neue", Impact, sans-serif; font-size: 44px; letter-spacing: 2px;
    color: var(--red); line-height: 1;
  }

  .badge { position: absolute; width: 136px; height: 136px; }
  .badge svg { position: absolute; inset: 0; }
  .badge__text { position: absolute; inset: 0; display: flex; flex-direction: column; align-items: center; justify-content: center; font-family: "Bebas Neue", Impact, sans-serif; text-align: center; }
  .badge__vip { font-size: 40px; line-height: .95; }
  .badge__sub { font-size: 17px; line-height: 1.08; }
  .flyer--front .badge { left: 335px; top: 319px; }
  .flyer--back .badge { left: 356px; top: 220px; }

  .question { position: absolute; left: 18px; top: 372px; font-family: "Bebas Neue", Impact, sans-serif; font-size: 29px; line-height: 29px; }

  .section-title { position: absolute; left: 18px; color: var(--red); font-weight: 700; font-size: 15.5px; letter-spacing: .2px; }
  .flyer--front .section-title { top: 471px; }
  .flyer--back .section-title { top: 490px; }

  .benefits { position: absolute; left: 18px; top: 505px; width: 490px; list-style: none; display: grid; grid-template-columns: 238px 240px; row-gap: 8px; }
  .benefit { display: flex; align-items: center; gap: 10px; height: 32px; font-size: 11.2px; line-height: 1.2; }
  .benefit__icon { flex: 0 0 32px; height: 32px; border-radius: 50%; background: var(--red); display: flex; align-items: center; justify-content: center; box-shadow: 0 0 0 2px rgba(210,32,47,.35); }

  .intro { position: absolute; left: 20px; top: 380px; width: 480px; font-size: 9.8px; line-height: 1.3; font-weight: 700; letter-spacing: -.25px; }
  .intro p + p { margin-top: 10px; }

  .services { position: absolute; left: 20px; top: 516px; width: 480px; list-style: none; display: grid; grid-template-columns: 250px 230px; grid-auto-flow: column; grid-template-rows: repeat(8, 17.3px); font-size: 11px; }
  .services li { display: flex; align-items: center; gap: 8px; }
  .services li::before { content: ""; width: 7px; height: 7px; border: 1.5px solid var(--red); border-radius: 50%; flex: 0 0 7px; }

  .contact-note { position: absolute; left: 20px; top: 670px; font-size: 9px; color: var(--muted); }

  .footer { position: absolute; left: 0; bottom: 0; width: 100%; height: 41px; background: var(--footer); }
  .footer__links { position: absolute; left: 0; top: 7px; height: 27px; width: 368px; background: var(--red); clip-path: polygon(0 0, 100% 0, 94% 100%, 0 100%); font-family: "Bebas Neue", Impact, sans-serif; font-size: 9.6px; letter-spacing: 0; display: flex; align-items: center; padding-left: 12px; white-space: nowrap; }
  .footer__phone { position: absolute; right: 12px; top: 7px; display: flex; align-items: center; gap: 7px; font-family: "Bebas Neue", Impact, sans-serif; font-size: 25px; letter-spacing: .4px; line-height: 27px; }
</style>
</head>
<body>

<section class="flyer flyer--front">
  <svg class="art" viewBox="0 0 515 731">
    <defs>
      <linearGradient id="carPhoto" x1="0" y1="0" x2="1" y2="1">
        <stop offset="0" stop-color="#b9bcc0"/>
        <stop offset=".45" stop-color="#b0131f"/>
        <stop offset="1" stop-color="#2a0a0c"/>
      </linearGradient>
    </defs>
    <g role="img" aria-label="Photo of a red sports car driving on a coastal road with mountains behind">
      <polygon points="0,68 515,68 515,283 153,360 0,305" fill="url(#carPhoto)"/>
    </g>
    <polygon points="0,305 153,360 515,283 515,297 153,378 0,320" fill="var(--red)"/>
    <polygon points="0,320 153,378 515,297 515,304 153,392 0,333" fill="var(--white)"/>
    <polygon points="0,333 153,392 515,304 515,309 153,398 0,338" fill="var(--red-dark)"/>
  </svg>

  <div class="brand">BRIGHTLANE TOTAL AUTOMOTIVE</div>

  <div class="question">TRADIE?<br>BUSINESS OWNER?<br>OWN 3 OR MORE VEHICLES?</div>

  <div class="badge">
    <svg viewBox="0 0 136 136"><circle cx="68" cy="68" r="60" fill="var(--red)" stroke="var(--red)" stroke-width="10" stroke-dasharray="6 4"/><circle cx="68" cy="68" r="58" fill="none" stroke="rgba(0,0,0,.18)" stroke-width="1"/></svg>
    <div class="badge__text"><span class="badge__vip">VIP</span><span class="badge__sub">FLEET VEHICLE<br>SERVICING AND<br>MAINTENANCE</span></div>
  </div>

  <h2 class="section-title">BECOME AN BRIGHTLANE VIP MEMBER AND RECEIVE:</h2>

  <ul class="benefits">
    <li class="benefit"><span class="benefit__icon"><svg width="16" height="16" viewBox="0 0 16 16"><path d="M3 8.5l3.2 3L13 4.5" fill="none" stroke="#fff" stroke-width="2.2"/></svg></span>10% off Vehicle Servicing and Mechanical Repairs</li>
    <li class="benefit"><span class="benefit__icon"><svg width="16" height="16" viewBox="0 0 16 16"><path d="M3 8.5l3.2 3L13 4.5" fill="none" stroke="#fff" stroke-width="2.2"/></svg></span>Vehicle Delivery and Pick up</li>
    <li class="benefit"><span class="benefit__icon"><svg width="16" height="16" viewBox="0 0 16 16"><path d="M3 8.5l3.2 3L13 4.5" fill="none" stroke="#fff" stroke-width="2.2"/></svg></span>10% off&nbsp;&nbsp;Tyres</li>
    <li class="benefit"><span class="benefit__icon"><svg width="16" height="16" viewBox="0 0 16 16"><path d="M3 8.5l3.2 3L13 4.5" fill="none" stroke="#fff" stroke-width="2.2"/></svg></span>Vehicle WOF, Service and Wheel Alignment reminders</li>
    <li class="benefit"><span class="benefit__icon"><svg width="16" height="16" viewBox="0 0 16 16"><path d="M3 8.5l3.2 3L13 4.5" fill="none" stroke="#fff" stroke-width="2.2"/></svg></span>Free basic vehicle exterior wash with every job</li>
    <li class="benefit"><span class="benefit__icon"><svg width="16" height="16" viewBox="0 0 16 16"><path d="M3 8.5l3.2 3L13 4.5" fill="none" stroke="#fff" stroke-width="2.2"/></svg></span>Given quick and first choice on all bookings and appointments</li>
    <li class="benefit"><span class="benefit__icon"><svg width="16" height="16" viewBox="0 0 16 16"><path d="M3 8.5l3.2 3L13 4.5" fill="none" stroke="#fff" stroke-width="2.2"/></svg></span>Free puncture repairs</li>
    <li class="benefit"><span class="benefit__icon"><svg width="16" height="16" viewBox="0 0 16 16"><path d="M3 8.5l3.2 3L13 4.5" fill="none" stroke="#fff" stroke-width="2.2"/></svg></span>Organise a tow truck to workshop for local break downs</li>
  </ul>

  <p class="contact-note">Contact us today to enquire about becoming an Brightlane VIP member.</p>

  <footer class="footer">
    <div class="footer__links">OFFICE@BRIGHTLANEAUTOMOTIVE-EXAMPLE.CO.NZ &nbsp;|&nbsp; WWW.BRIGHTLANEAUTOMOTIVE-EXAMPLE.CO.NZ</div>
    <div class="footer__phone"><svg width="13" height="22" viewBox="0 0 13 22"><rect x="1" y="1" width="11" height="20" rx="2" fill="none" stroke="#fff" stroke-width="1.6"/><line x1="5" y1="18" x2="8" y2="18" stroke="#fff" stroke-width="1.4"/></svg>07 842 3917</div>
  </footer>
</section>

<section class="flyer flyer--back">
  <svg class="art" viewBox="0 0 515 731">
    <defs>
      <linearGradient id="shopPhoto" x1="0" y1="0" x2="1" y2="1">
        <stop offset="0" stop-color="#e4e4e2"/>
        <stop offset=".5" stop-color="#9a9a98"/>
        <stop offset="1" stop-color="#5a1c20"/>
      </linearGradient>
    </defs>
    <g role="img" aria-label="Photo of a white car raised on a red hoist in a workshop with a tyre on the floor">
      <polygon points="0,68 515,68 515,270 145,350 0,280" fill="url(#shopPhoto)"/>
    </g>
    <polygon points="0,280 145,350 515,270 515,283 145,366 0,293" fill="var(--white)"/>
    <polygon points="0,293 145,366 515,283 515,292 145,376 0,300" fill="var(--red)"/>
  </svg>

  <div class="brand">BRIGHTLANE TOTAL AUTOMOTIVE</div>

  <div class="badge">
    <svg viewBox="0 0 136 136"><circle cx="68" cy="68" r="60" fill="var(--red)" stroke="var(--red)" stroke-width="10" stroke-dasharray="6 4"/><circle cx="68" cy="68" r="58" fill="none" stroke="rgba(0,0,0,.18)" stroke-width="1"/></svg>
    <div class="badge__text"><span class="badge__vip">VIP</span><span class="badge__sub">FLEET VEHICLE<br>SERVICING AND<br>MAINTENANCE</span></div>
  </div>

  <div class="intro">
    <p>If you’ve got a fleet of vehicles for your business, Brightlane can make it easy for you to stay on top of your servicing and maintenance schedules. We offer peace of mind motoring that ensures your vehicles are safe and reliable at cost effective prices.</p>
    <p>Brightlane is your one stop automotive shop. We aim to make your automotive servicing and repairs as easy and painless as possible. We pride ourselves on excellent customer service and quality workmanship in a professional manner at competitive rates, using the latest technology and equipment.</p>
  </div>

  <h2 class="section-title">OUR SERVICES INCLUDE:</h2>

  <ul class="services">
    <li>Vehicle Servicing</li>
    <li>All Mechanical Repairs</li>
    <li>Brakes, steering and suspension</li>
    <li>Transmission and cooling system servicing</li>
    <li>Warrant of fitness inspections</li>
    <li>Safety checks and pre-purchase inspections</li>
    <li>Tyres and wheel alignments</li>
    <li>Puncture repairs</li>
    <li>Mag wheels</li>
    <li>Vehicle Lowering and lift kits</li>
    <li>Automotive diagnostics</li>
    <li>Trailer repairs, maintenance and parts</li>
    <li>Automotive parts and supplies</li>
    <li>4WD accessories</li>
    <li>Batteries</li>
    <li>And more</li>
  </ul>

  <p class="contact-note">Contact us today to enquire about becoming an Brightlane VIP member.</p>

  <footer class="footer">
    <div class="footer__links">OFFICE@BRIGHTLANEAUTOMOTIVE-EXAMPLE.CO.NZ &nbsp;|&nbsp; WWW.BRIGHTLANEAUTOMOTIVE-EXAMPLE.CO.NZ</div>
    <div class="footer__phone"><svg width="13" height="22" viewBox="0 0 13 22"><rect x="1" y="1" width="11" height="20" rx="2" fill="none" stroke="#fff" stroke-width="1.6"/><line x1="5" y1="18" x2="8" y2="18" stroke="#fff" stroke-width="1.4"/></svg>07 842 3917</div>
  </footer>
</section>

</body>
</html>
```